Drink Product Brochure

We have 3 tea drinks in plastic bottles that we'd like to put in a brochure (8"x11" sheet) and focus on all natural, no preservatives, and supporting a nonprofit orphanage. The logo boasts a one color design - green. The brochure should make 3-4 key highlights, and allow at least one section product overview. Clean, modern design with not to many distractions but an inviting natural look and highlight the key features.

Target Market(s)

Middle age

Font styles to use
Serif
Sans Serif

Colors
add136
85cae6
b768aa

```html
<!DOCTYPE html>
<html lang="de">
<head>
<meta charset="utf-8">
<title>Tea &amp; Coffee Ready to Drink – Brochure</title>
<link rel="stylesheet" href="https://fonts.googleapis.com/css2?family=Montserrat:wght@400;600;700;800&family=Open+Sans:wght@400;600;700&family=Roboto+Condensed:wght@400;700&display=swap">
<style>
:root{
  --green:#add136;
  --green-dark:#8fb52a;
  --blue:#85cae6;
  --blue-deep:#1e73be;
  --purple:#b768aa;
  --ink:#333;
  --paper:#fff;
  --bg:#e4e4e4;
  --head:"Montserrat",sans-serif;
  --body:"Open Sans",sans-serif;
  --cond:"Roboto Condensed",sans-serif;
}
*{box-sizing:border-box;margin:0;padding:0}
html,body{width:1200px;height:1200px;overflow:hidden;background:var(--bg)}
.stage{position:absolute;left:0;top:0;width:1500px;height:1500px;transform:scale(.8);transform-origin:0 0}
.brochure{position:absolute;background:var(--paper);display:flex}
.brochure--outside{left:92px;top:55px;width:852px;height:657px}
.brochure--inside{left:551px;top:771px;width:851px;height:659px}
.panel{position:relative;width:284px;height:100%;overflow:hidden}
.abs{position:absolute}
.photo{position:absolute}
.logo-name{font-family:var(--head);font-weight:700;color:var(--green-dark);font-size:15px;display:flex;align-items:center;gap:6px}
.logo-name i{display:inline-block;width:12px;height:12px;background:var(--green-dark)}

/* outside – panel 1 */
.intro-band{position:absolute;left:0;top:0;width:284px;height:190px;background:linear-gradient(90deg,var(--green),#bedb5a)}
.intro-title{left:26px;top:22px;font:700 14.5px/1.1 var(--head);color:#fff;letter-spacing:.3px}
.intro-frame{position:absolute;left:52px;top:95px;width:180px;height:190px;background:#fff;border-radius:0 0 90px 90px}
.intro-photo{left:115px;top:118px;width:56px;height:148px;border-radius:14px 14px 8px 8px;background:linear-gradient(#c3e35a,#7cc23a 70%,#d9b24a)}
.subhead{font:700 12.5px/1.15 var(--head);color:var(--blue)}
.copy{font:400 10px/1.3 var(--body);color:var(--ink);text-align:justify}
.foot-band{position:absolute;left:0;bottom:0;width:100%;height:67px;background:var(--purple);color:#fff;font:700 10px/1.25 var(--body);text-align:center;padding-top:22px}

/* outside – panel 2 */
.steps-band{position:absolute;left:0;top:0;width:284px;height:70px;background:var(--green)}
.steps-title{left:50px;top:38px;font:700 14px var(--head);color:#fff;letter-spacing:.3px}
.steps{left:50px;top:100px;width:200px;font:400 10.5px/1.05 var(--body);color:var(--ink)}
.steps b{font-family:var(--head);font-weight:700;font-size:12.5px}
.steps p{margin-bottom:12px}
.cta-box{left:56px;top:292px;width:164px;height:60px;background:#f4f4f4;border-radius:6px;box-shadow:0 2px 4px rgba(0,0,0,.25);font:400 12.5px/1.1 var(--body);text-align:center;padding-top:12px;color:var(--ink)}
.cta-button{left:48px;top:344px;width:182px;height:46px;border-radius:10px;background:linear-gradient(#3aa0e8,var(--blue-deep));color:#fff;text-align:center;font:700 12px/1.2 var(--body);padding-top:6px;box-shadow:0 4px 5px rgba(0,0,0,.3)}
.cta-button span{font-weight:400;font-size:15px}
.contact{position:absolute;left:0;bottom:0;width:284px;height:191px;background:var(--purple);color:#fff}
.contact-main{left:64px;top:22px;font:400 12.5px/1.1 var(--head)}
.contact-main b{font-weight:700;font-size:14px;display:block}
.contact-line{left:64px;font:400 12.5px var(--head)}
.rule{position:absolute;left:64px;width:176px;border-top:1px dashed rgba(255,255,255,.6)}
.icon{position:absolute;left:32px}

/* outside – panel 3 */
.cover-title{left:38px;top:30px;font:800 50px/.84 var(--head)}
.cover-title .light{color:transparent;-webkit-text-stroke:1px #cfcfcf;font-weight:400;font-size:46px}
.cover-title .p{color:var(--purple)}
.cover-title .b{color:var(--blue)}
.cover-title .g{color:var(--green)}
.cover-photo{left:0;top:410px;width:284px;height:247px;background:radial-gradient(circle at 50% 60%,#f4d64a 0,#e48a2a 30%,#79b941 60%,#add136 100%)}

/* inside – panel 1 */
.stat-title{left:34px;top:30px;font:700 13.5px/1.4 var(--cond);color:#fff}
.stat-pct{left:140px;top:64px;font:700 23px var(--cond);color:#e4312b}
.stat-bar{position:absolute;background:#ee5a35;border-radius:4px 4px 2px 2px}
.stat-year{position:absolute;top:178px;width:42px;background:#222;color:#fff;font:700 14px/18px var(--cond);text-align:center}
.stat-src{left:198px;top:113px;font:400 9px/1.4 var(--cond);color:var(--ink)}
.blue-head{font:700 16px/1.2 var(--head);color:var(--blue-deep)}
.cond{font:400 10.5px/1.25 var(--cond);color:var(--ink)}
.cond p{margin-bottom:10px}

/* inside – panel 2 */
.products-title{left:25px;top:22px;font:700 23px/.95 var(--head);color:var(--blue);letter-spacing:.5px;z-index:2}
.products-green{position:absolute;left:0;top:175px;width:284px;height:484px;background:var(--green)}
.lead{font:700 12.5px/1.2 var(--head);color:#fff}
.green-copy{left:36px;top:252px;width:218px;font:400 9.8px/1.3 var(--cond);color:#fff}
.green-copy p{margin-bottom:10px}
.green-copy b{font-weight:700}
.system{left:34px;top:430px;font:700 15px var(--head);color:#222}
.system span{font-weight:400}
.sizes{left:66px;top:470px;width:150px;height:112px;background:linear-gradient(90deg,var(--blue-deep),#3aa0e8)}
.sizes-caption{left:0;top:596px;width:284px;text-align:center;font:700 10.5px/1.2 var(--head);color:#222}

/* inside – panel 3 */
.benefits-title{left:26px;top:190px;font:700 21px var(--head);color:var(--purple)}
.benefits-sub{left:26px;top:218px;font:700 14px/1.2 var(--head);color:var(--purple)}
.benefits{left:26px;top:266px;width:192px;font:400 9px/1.3 var(--cond);color:var(--ink)}
.benefits p{margin-bottom:10px}
.benefits b{font-weight:700}
.strip{position:absolute;left:0;bottom:0;width:100%;height:9px;background:var(--purple)}
</style>
</head>
<body>
<main class="stage">

  <!-- Outside spread -->
  <section class="brochure brochure--outside">
    <article class="panel">
      <div class="intro-band"></div>
      <h2 class="abs intro-title">INNOVATIVE<br>TECHNOLOGIE</h2>
      <div class="intro-frame"></div>
      <div class="photo intro-photo" role="img" aria-label="Green tea bottle product photo"></div>
      <h3 class="abs subhead" style="left:26px;top:285px">THE BEST PORTABLE TEA<br>INFUSER BOTTLES OF 2018</h3>
      <p class="abs copy" style="left:26px;top:346px;width:233px">This infuser is absolutely beautiful to look at. Glass bottles are awesome because you can see exactly what you’re brewing. This creates a much more elegant experience than a tea thermos. Another benefit of glass is that it is easy to clean.</p>
      <h3 class="abs" style="left:26px;top:445px;font:600 12px var(--body);color:var(--blue)">Gut zu wissen</h3>
      <p class="abs copy" style="left:26px;top:475px;width:233px">This bottle is both beautiful and practical. The exterior has a comfortable matte finish that won’t slip out of your hand and the bottle is both durable and light. The bottle is made out of a vacuum insulated stainless steel that is non-toxic and will keep your drinks hot or cold for hours at a time.</p>
      <div class="foot-band">Das gute GEFÜHL<br>von NATUR pur!</div>
    </article>

    <article class="panel">
      <div class="steps-band"></div>
      <h2 class="abs steps-title">SO EINFACHGEHT´S</h2>
      <div class="abs steps">
        <p><b>1.Anrufen</b><br>Jetzt einfach anrufen unter:<br><strong>0221 480 163 52</strong></p>
        <p><b>2.Probierpaket bestellen und</b></p>
        <p><b>3.zu Hause testen</b><br>Natürlich absolut kostenfrei und<br>völlig unverbindlich für Sie!</p>
        <p>Denn nur so können Sie am besten herausfinden, welche Teesorte wirklich die Richtige für Ihren ganz persönlichen Geschmack ist.</p>
      </div>
      <div class="abs cta-box">Jetzt kostenfrei und<br>unverbindlich testen!</div>
      <div class="abs cta-button">Beratung unter<br><span>0221 480 163 50</span></div>
      <div class="abs logo-name" style="left:98px;top:422px">Verdanta Tea <i></i></div>
      <div class="contact">
        <svg class="icon" style="top:26px" width="14" height="18" viewBox="0 0 14 18"><path d="M7 0a7 7 0 0 1 7 7c0 5-7 11-7 11S0 12 0 7a7 7 0 0 1 7-7z" fill="#fff"/><circle cx="7" cy="7" r="2.6" fill="var(--purple)"/></svg>
        <p class="abs contact-main"><b>VERDANTA TEA</b>Natürlicher Eistee<br>der nächsten Generation<br>by Halvex GmbH<br>Lindenstraße 12 50674 Köln<br>Kundenservice: 0221 480 163 50</p>
        <div class="rule" style="top:116px"></div>
        <svg class="icon" style="top:128px" width="14" height="10" viewBox="0 0 14 10"><rect x=".5" y=".5" width="13" height="9" fill="none" stroke="#fff"/><path d="M.5.5 7 6 13.5.5" fill="none" stroke="#fff"/></svg>
        <p class="abs contact-line" style="top:124px">info@verdanta-tea.de</p>
        <div class="rule" style="top:144px"></div>
        <svg class="icon" style="top:154px" width="13" height="13" viewBox="0 0 13 13"><circle cx="6.5" cy="6.5" r="6" fill="none" stroke="#fff"/><path d="M.5 6.5h12M6.5.5c-3 3-3 9 0 12M6.5.5c3 3 3 9 0 12" fill="none" stroke="#fff" stroke-width=".8"/></svg>
        <p class="abs contact-line" style="top:152px;font-weight:700;font-size:14px">www.verdanta-tea.de</p>
      </div>
    </article>

    <article class="panel">
      <h1 class="abs cover-title"><span class="light">TEA &amp;<br>COFFEE</span><br><span class="p">READY</span><br><span class="b">TO</span><br><span class="g">DRINK</span></h1>
      <div class="abs logo-name" style="left:42px;top:292px">Verdanta Tea <i></i></div>
      <svg class="abs" style="left:0;top:0" width="284" height="657" viewBox="0 0 284 657">
        <path d="M80 378C180 378 262 260 284 125L284 175C256 300 172 392 80 378Z" fill="var(--blue)"/>
        <path d="M0 372C110 412 246 320 284 205L284 262C238 372 110 420 0 392Z" fill="var(--purple)"/>
        <path d="M0 398C118 430 250 372 284 290L284 657L0 657Z" fill="var(--green)"/>
      </svg>
      <div class="photo cover-photo" role="img" aria-label="Three iced tea bottles with lemon, peach and mint leaves on ice"></div>
    </article>
  </section>

  <!-- Inside spread -->
  <section class="brochure brochure--inside">
    <article class="panel">
      <svg class="abs" style="left:0;top:0" width="284" height="250" viewBox="0 0 284 250">
        <path d="M0 0H262C140 36 26 120 12 240H0Z" fill="var(--blue)"/>
        <path d="M262 0C140 36 26 120 12 240" fill="none" stroke="#d6d6d6" stroke-width="6"/>
      </svg>
      <p class="abs stat-title">Die Zahl der<br>Teetrinker<br>steigt!</p>
      <p class="abs stat-pct">53%</p>
      <svg class="abs" style="left:105px;top:85px" width="50" height="36" viewBox="0 0 50 36"><path d="M4 34C6 14 22 4 44 4" fill="none" stroke="#333" stroke-dasharray="2 2"/><path d="M40 0 46 4 40 8" fill="none" stroke="#333"/></svg>
      <div class="stat-bar" style="left:94px;top:118px;width:18px;height:58px"></div>
      <div class="stat-bar" style="left:152px;top:92px;width:24px;height:84px"></div>
      <div class="stat-year" style="left:82px">2004</div>
      <div class="stat-year" style="left:143px">2015</div>
      <p class="abs stat-src">Quelle:<br>Deutscher<br>Teemarktbericht<br>2015 teeverband-stat.de</p>
      <h2 class="abs blue-head" style="left:26px;top:216px;width:250px">Alle 2 Minuten wird in Deutschland Eistee gekauft.</h2>
      <div class="abs cond" style="left:26px;top:266px;width:233px;text-align:justify"><p>Neben dem erfrischenden Geschmack zählt für viele Menschen heute vor allem, was wirklich in der Flasche steckt – natürliche Zutaten, wenig Zucker und ein gutes Gewissen beim Genießen.</p></div>
      <h2 class="abs blue-head" style="left:26px;top:353px;font-size:14.5px">Was zählt, ist die Natur...</h2>
      <div class="abs cond" style="left:26px;top:381px;width:236px">
        <p><b>93%</b> der Befragten achten beim Einkauf auf Zutaten – bei Getränken sogar noch mehr als früher.</p>
        <p>Jeder 10te Kunde wünscht sich <b>Tee ganz ohne Konservierungsstoffe</b> (jeder 8. ohne Farbstoffe und jeder 4. mit weniger Zucker bzw. reinem Blattaroma) ...</p>
        <p>In jedem 5. Haushalt (20,1 %) <b>wird täglich Tee getrunken</b></p>
        <p>Mit jeder Flasche unterstützen Sie zudem ein gemeinnütziges Waisenhaus. Deshalb steht Verdanta Tea für <u>Verantwortung</u>, insbesondere durch:</p>
        <p style="font-size:11.5px;line-height:1.3">1. rein natürliche Zutaten<br>2. keine Konservierungsstoffe und<br>3. Unterstützung eines Waisenhauses</p>
      </div>
      <div class="strip"></div>
    </article>

    <article class="panel">
      <h2 class="abs products-title">OUR<br>PRODUCTS</h2>
      <div class="photo" style="left:25px;top:92px;width:105px;height:68px;background:linear-gradient(90deg,#e8463a,#2f9fd8,#8b56b3)" role="img" aria-label="Row of small colourful drink bottles"></div>
      <div class="photo" style="left:178px;top:18px;width:90px;height:157px;border-radius:30px 30px 0 0;background:linear-gradient(#e8e8e8 0,#e8e8e8 20%,#5fbf3a 40%,#1f7f2a)" role="img" aria-label="Green tea bottle with leaves on the label"></div>
      <div class="products-green"></div>
      <p class="abs lead" style="left:24px;top:204px;width:250px">In 95% der Fälle greifen Kunden wieder zu, wenn sie einmal probiert haben.</p>
      <div class="abs green-copy">
        <p><b>Genießen Sie daher heute noch einen Eistee der nächsten Generation – ganz natürlich, für sich und Ihre Familie!</b></p>
        <p><b>Ein Anruf genügt – wir beraten Sie gerne.</b></p>
        <p>Egal ob Grüntee, Früchtetee oder Schwarztee – zu Hause, im Büro oder unterwegs – alle drei Sorten kommen ohne Konservierungsstoffe aus.</p>
        <p><b>Nutzen Sie diese Aktion und testen Sie jetzt einfach kostenfrei bei sich zu Hause:</b></p>
      </div>
      <p class="abs system">Die neue Verdanta <span>– Serie</span></p>
      <div class="photo sizes" role="img" aria-label="Blue bottle icons in five sizes from 1500 ml to 250 ml"></div>
      <p class="abs sizes-caption">Der wahrscheinlich natürlichste<br>Eistee der Welt</p>
      <div class="strip"></div>
    </article>

    <article class="panel">
      <div class="photo" style="left:30px;top:0;width:120px;height:170px;border-radius:0 0 30px 30px;background:linear-gradient(90deg,#c9b437,#f2e78a,#b8a22a)" role="img" aria-label="Clear bottle filled with golden tea"></div>
      <div class="photo" style="left:222px;top:86px;width:62px;height:366px;border-radius:30px 0 0 20px;background:linear-gradient(#eee 0,#eee 8%,#d8c53c 18%,#f3e36a 55%,#c6b230)" role="img" aria-label="Bottle of golden tea with lemon label, partly cut off"></div>
      <h2 class="abs benefits-title">Ihre Vorteile:</h2>
      <p class="abs benefits-sub">Öffnen – Einschenken<br>GENIESSEN!</p>
      <div class="abs benefits">
        <p><b>Keine Konservierungsstoffe</b><br>(nur echte Teeblätter, Früchte und Wasser).</p>
        <p>Der Tee wird frisch aufgebrüht, <b>BEVOR</b> er<br><br>schonend in die Flasche gelangt.</p>
        <p><b>Ursprünglich nach Familienrezept entwickelt,</b> mit natürlichem Aroma aus Zitrone, Pfirsich und Minze.</p>
        <p>Frei von Farbstoffen und Süßstoffen.</p>
        <p><b>Praktische Flasche, wiederverschließbar</b> und ideal für unterwegs.</p>
        <p>Sie &amp; Ihre Liebsten genießen mit gutem Gewissen. <b>Für ein Waisenhaus!</b></p>
        <p><b>Optimal für den ganzen Tag</b><br>kein Aufbrühen, kein Abkühlen, kein Teebeutel nötig, <b>einfach kalt genießen.</b></p>
        <p>Sofort trinkbereit!</p>
        <p>Bereits ab 1,90 € (inkl. MwSt.) pro Flasche, ein Teil davon geht an unser Partner-Waisenhaus. Jetzt anrufen, Probierpaket bestellen und kostenfrei testen.</p>
      </div>
      <div class="strip"></div>
    </article>
  </section>

</main>
</body>
</html>
```